Banners for Affiliate Marketing on Tantra website

We are starting an affiliate marketing program on our website brightmeadowhub.com and need banner ads for our affiliates. We are looking for the following sizes

for sure: 728x90, 300x250, 160x600
possibly: 468x60, 250x250, 125x125

Banner ads should market a several of our products - online tantra store, various tantra workshops, tantra vacations. See our website for details on what we offer.

For example, EITHER we may need one banner ad each in different sizes for:

Women's Workshop
Tantra Vacations
Tantric Massage workshop
Amber Harbor workshop
Sunrise & Willow Training
Selected products from our store, for example Quiet River Evenings DVD, or Milbrook Package

OR maybe we just need one banner ad in all the sizes for
Workshops
Store
Vacations

All images on our site can be used, or use other stock images.

The winner of this project will continue to work with us on graphic design of future banners, and we are also looking for a logo design.

Target Market(s)

couples, singles, age group 28-65, with disposable income

Industry/Entity Type

Graphic Design

Requirements
Must have
• Modern, attractive design that matches the branding and coloring on our website.
Should not have
• no obvious nudity in any graphics

```html
<!DOCTYPE html>
<html lang="en">
<head>
<meta charset="utf-8">
<title>Workshops Banner</title>
<link rel="stylesheet" href="https://fonts.googleapis.com/css2?family=Tinos:wght@700&display=swap">
<style>
  :root {
    --brand-red: #a5140f;
    --brand-red-deep: #6a0806;
    --gold: #f2c230;
    --skin-shadow: #8a5535;
    --skin-warm: #c4875a;
    --skin-mid: #d9a77c;
    --skin-light: #ecc9a9;
    --skin-pale: #f6e4d6;
    --text-light: #ffffff;
  }
  html, body {
    margin: 0;
    padding: 0;
    width: 1200px;
    height: 148px;
    overflow: hidden;
    background: #ffffff;
  }
  .banner {
    position: relative;
    width: 1200px;
    height: 148px;
    overflow: hidden;
    background: var(--skin-warm);
  }
  .photo-massage {
    position: absolute;
    left: 0;
    top: 0;
    width: 790px;
    height: 148px;
    background:
      radial-gradient(ellipse 160px 60px at 470px 60px, rgba(245,205,170,0.7), rgba(245,205,170,0) 100%),
      radial-gradient(ellipse 120px 40px at 420px 118px, rgba(250,215,185,0.6), rgba(250,215,185,0) 100%),
      radial-gradient(ellipse 200px 70px at 560px 10px, rgba(95,50,30,0.55), rgba(95,50,30,0) 100%),
      radial-gradient(ellipse 220px 90px at 640px 130px, rgba(150,95,60,0.5), rgba(150,95,60,0) 100%),
      linear-gradient(100deg, #b86f4a 0%, var(--skin-mid) 25%, var(--skin-warm) 45%, #e0b08a 62%, #a86a44 85%, #c99670 100%);
  }
  .photo-face {
    position: absolute;
    left: 740px;
    top: 0;
    width: 460px;
    height: 148px;
    background:
      radial-gradient(ellipse 90px 130px at 420px 80px, rgba(235,200,170,0.9), rgba(235,200,170,0) 100%),
      radial-gradient(ellipse 150px 60px at 180px 110px, rgba(248,228,212,0.95), rgba(248,228,212,0) 100%),
      radial-gradient(ellipse 180px 50px at 260px 20px, rgba(170,120,90,0.55), rgba(170,120,90,0) 100%),
      linear-gradient(90deg, rgba(210,160,125,0) 0%, var(--skin-light) 18%, var(--skin-pale) 45%, var(--skin-light) 75%, #d7a783 100%);
  }
  .brand-panel {
    position: absolute;
    left: 0;
    top: 0;
    width: 200px;
    height: 148px;
  }
  .topband {
    position: absolute;
    left: 0;
    top: 0;
    width: 780px;
    height: 12px;
    background: linear-gradient(90deg, var(--brand-red-deep) 0%, rgba(106,8,6,0.85) 50%, rgba(106,8,6,0) 100%);
  }
  .brand-mark {
    position: absolute;
    left: 7px;
    top: 3px;
    width: 142px;
    height: 142px;
    border-radius: 50%;
    border: 3px solid var(--gold);
    box-sizing: border-box;
    display: flex;
    align-items: center;
    justify-content: center;
    text-align: center;
  }
  .brand-name {
    font-family: "Tinos", serif;
    font-weight: 700;
    font-size: 16px;
    line-height: 1.2;
    color: var(--gold);
  }
  .banner-title {
    position: absolute;
    left: 164px;
    top: 88px;
    margin: 0;
    font-family: "Tinos", serif;
    font-weight: 700;
    font-size: 38px;
    line-height: 1;
    color: var(--text-light);
    text-shadow: 2px 2px 3px rgba(0,0,0,0.6);
  }
</style>
</head>
<body>
  <div class="banner">
    <div class="photo-massage" role="img" aria-label="Close-up photo of hands giving a relaxing back massage"></div>
    <div class="photo-face" role="img" aria-label="Photo of a relaxed woman receiving a gentle head massage"></div>
    <svg class="brand-panel" viewBox="0 0 200 148" aria-hidden="true">
      <defs>
        <linearGradient id="panelFade" x1="0" y1="0" x2="1" y2="0">
          <stop offset="0" stop-color="#a5140f"/>
          <stop offset="0.72" stop-color="#a5140f"/>
          <stop offset="1" stop-color="#a5140f" stop-opacity="0.85"/>
        </linearGradient>
      </defs>
      <path d="M0 0 H170 C150 40 155 100 190 148 H0 Z" fill="url(#panelFade)"/>
    </svg>
    <div class="topband"></div>
    <div class="brand-mark">
      <span class="brand-name">Bright<br>Meadow<br>Hub</span>
    </div>
    <h1 class="banner-title">Workshops</h1>
  </div>
</body>
</html>
```